Ventrox Corporate General Presentation

Ventrox is a leading player in ICT (Information Communication Technology) cooling, we need a design for our corporate general presentation.

Attached is a reference of content

Our logo main color is industrial blue, our technology is green (energy saving).

existing website: www.ven-trox.example www.ven-trox.example.uk

Hi, this is a package with USD 620 for PPT and 290 for 5 web pages, plus 100 each for number 2 and 3 position in the tender Added Wednesday, December 30, 2015

Target Market(s)

Global

Industry/Entity Type

Communication

Number of Pages Required

5+ page

Font styles to use
Serif
Sans Serif

Colors
0255a3
3176b5
0293ce
33a6d7
9bcb3c

```html
<!DOCTYPE html>
<html lang="en">
<head>
<meta charset="UTF-8">
<title>Ventrox – Business Strategies</title>
<link href="https://fonts.googleapis.com/css2?family=Oswald:wght@600;700&family=Roboto+Condensed:wght@400;700&display=swap" rel="stylesheet">
<style>
  :root {
    --blue-deep: #0255a3;
    --blue-mid: #3176b5;
    --blue-bright: #0293ce;
    --blue-light: #33a6d7;
    --card-dark: #0a5fae;
    --card-light: #3497db;
    --green: #9bcb3c;
    --ink: #2a2a2a;
    --grey: #6e6e6e;
    --page: #f3f5f7;
    --footer: #e9ebed;
  }
  * { margin: 0; padding: 0; box-sizing: border-box; }
  html, body { width: 1200px; height: 900px; overflow: hidden; }
  body {
    font-family: "Roboto Condensed", "Arial Narrow", sans-serif;
    background: var(--page);
    position: relative;
  }
  .backdrop {
    position: absolute; inset: 87px 0 51px 0;
    background: linear-gradient(180deg, #eef1f4 0%, #f8f9fa 55%, #eceff2 100%);
  }
  .header {
    position: absolute; top: 0; left: 0; width: 1200px; height: 87px;
  }
  .header svg { position: absolute; inset: 0; }
  .header__title {
    position: absolute; left: 21px; top: 18px;
    font-family: "Oswald", "Arial Narrow", sans-serif;
    font-weight: 700; font-size: 36px; letter-spacing: 1px;
    color: #fff; line-height: 1;
    word-spacing: 8px;
  }
  .brand {
    position: absolute; right: 32px; top: 0; height: 87px;
    display: flex; align-items: center;
    font-family: "Roboto Condensed", sans-serif; font-weight: 700;
    font-size: 32px; line-height: 1; color: #fff;
  }
  .lead {
    position: absolute; left: 54px; top: 128px;
    font-weight: 700; font-size: 27px; color: var(--blue-deep);
  }
  .card {
    position: absolute; top: 187px; width: 318px; height: 418px;
    border: 3px solid #fff;
    box-shadow: 0 1px 4px rgba(0,0,0,0.15);
    background: var(--card-dark);
    color: #fff;
  }
  .card--telecom { background: var(--card-light); }
  .card__head {
    height: 63px; display: flex; align-items: center; justify-content: center;
    font-weight: 700; font-size: 27px;
  }
  .card__photo { height: 189px; border-top: 2px solid #fff; border-bottom: 3px solid #fff; }
  .card__photo--dc { background: linear-gradient(180deg, #9fb0bd 0%, #5d6c78 45%, #cfd8de 100%); }
  .card__photo--tel { background: linear-gradient(180deg, #8f8a7e 0%, #c9c4ba 40%, #e6e8ea 70%, #9a9386 100%); }
  .card__photo--med { background: linear-gradient(180deg, #b9bcbe 0%, #e8eaeb 50%, #a7aaad 100%); }
  .card__list {
    list-style: none; padding: 12px 0 0 20px;
    font-size: 21px; line-height: 34.5px;
  }
  .card__list li::before { content: "•"; margin-right: 10px; font-size: 16px; vertical-align: 2px; }
  .core {
    position: absolute; left: 55px; top: 640px;
    font-weight: 700; font-size: 27px; color: var(--grey);
    padding-bottom: 4px; border-bottom: 2px solid #9a9a9a;
  }
  .core__accent { color: var(--blue-deep); }
  .points { position: absolute; left: 55px; top: 692px; }
  .points p { font-size: 19px; color: var(--ink); height: 40.5px; line-height: 32px; }
  .points strong { color: var(--blue-deep); font-size: 24px; font-weight: 700; }
  .footer {
    position: absolute; left: 0; bottom: 0; width: 1200px; height: 51px;
    background: var(--footer); border-top: 2px solid #d7dadd;
    display: flex; align-items: center; justify-content: space-between;
    padding: 0 18px; font-weight: 700; font-size: 16px; color: #4d4d4d;
  }
</style>
</head>
<body>
  <div class="backdrop" role="img" aria-label="Faint data centre server hall background"></div>

  <header class="header">
    <svg width="1200" height="87" viewBox="0 0 1200 87" aria-hidden="true">
      <defs>
        <linearGradient id="bandLeft" x1="0" y1="0" x2="0" y2="1">
          <stop offset="0" stop-color="#1a6cbd"/>
          <stop offset="1" stop-color="#0255a3"/>
        </linearGradient>
        <linearGradient id="bandRight" x1="0" y1="0" x2="0" y2="1">
          <stop offset="0" stop-color="#2c86d2"/>
          <stop offset="1" stop-color="#1470c0"/>
        </linearGradient>
      </defs>
      <rect width="1200" height="87" fill="url(#bandLeft)"/>
      <polygon points="930,0 1200,0 1200,87 975,87" fill="url(#bandRight)"/>
      <polygon points="897,0 915,0 960,87 942,87" fill="#ffffff"/>
      <polygon points="918,0 926,0 971,87 963,87" fill="#7fc0ec"/>
    </svg>
    <h1 class="header__title">BUSINESS STRATEGIES</h1>
    <div class="brand">Ventrox</div>
  </header>

  <h2 class="lead">Global leader in ICT and Medical Equipment Cooling</h2>

  <section class="card card--datacenter" style="left:56px;">
    <div class="card__head">Data Center 40%</div>
    <div class="card__photo card__photo--dc" role="img" aria-label="Data centre aisle with rows of server racks"></div>
    <ul class="card__list">
      <li>Close Control A/C</li>
      <li>Chillers</li>
      <li>High Heat Density Product</li>
      <li>Engineering, Consulting</li>
    </ul>
  </section>

  <section class="card card--telecom" style="left:433px;">
    <div class="card__head">Telecom 30%</div>
    <div class="card__photo card__photo--tel" role="img" aria-label="Two outdoor shelter air conditioning units mounted on a wall"></div>
    <ul class="card__list">
      <li>BTS Shelter A/C, FCB</li>
      <li>Cabinet Cooling</li>
      <li>Energy Saving Solution</li>
      <li>System Integration</li>
    </ul>
  </section>

  <section class="card card--medical" style="left:810px;">
    <div class="card__head">Medical 30%</div>
    <div class="card__photo card__photo--med" role="img" aria-label="Medical CT scanner with patient table"></div>
    <ul class="card__list">
      <li>Medical Chillers</li>
      <li>Heat Exchangers</li>
      <li>Integrated Cooling</li>
      <li>Solution</li>
    </ul>
  </section>

  <h3 class="core"><span class="core__accent">Core</span> Competitiveness</h3>

  <div class="points">
    <p><strong>State of the Art Technology :</strong>&nbsp; energy saving, intelligent control, high reliability.</p>
    <p><strong>Speed :</strong> R&amp;D resource, concept&nbsp; to prototype &lt;6weeks, vertical integrated manufacturing.</p>
    <p><strong>Best TCO :</strong> China-based Cost Advantage, best Opex saving. Highly Standardization on component selection.</p>
  </div>

  <footer class="footer">
    <span>COPYRIGHT TEXT HERE</span>
    <span>PAGE : 01</span>
  </footer>
</body>
</html>
```